Training Company Needs a Web Design

We are a Training company that needs a website design completed for us. "The Harbor Loft" The website will be a 'community space' specialising in 'Change and Transformation'. It will be a 'space' where individuals can come to find out 'latest news', upcoming events and courses, chat with others and find 'tools and templates'. They will need to login as a 'Member'.

The final design needs to be professional but have a 'fun and interactive' feel and appeal to our target audience who are predominantly corporate individuals.

Target Market(s)

Corporate Individuals - they may have a Change or Project background

Industry/Entity Type

Business Consultant

Number of Pages Required

3 page

Font styles to use
Sans Serif

Requirements
Must have
• Design for 'Home Page'
• A professional and corporate 'feel' but be fun and interactive.
Nice to have
• A 'sense' of how some of the other pages may be designed or laid out.

```html
<!DOCTYPE html>
<html lang="en">
<head>
<meta charset="utf-8">
<title>The Harbor Loft – Home</title>
<link rel="stylesheet" href="https://fonts.googleapis.com/css2?family=Open+Sans:wght@300;400;600;700&family=Roboto+Condensed:wght@400;700&display=swap">
<style>
  :root {
    --page: #e8e8e8;
    --white: #ffffff;
    --navy: #0d3f6e;
    --band: #0a5089;
    --band-dark: #07406f;
    --brand: #1b6fae;
    --cyan: #1fb8c9;
    --accent: #1a9fd4;
    --ink: #1c1c1c;
    --body: #5c5c5c;
    --muted: #8a8a8a;
    --field: #e4e4e4;
    --red: #e2502c;
    --yellow: #e9c23a;
    --blue: #1496d8;
    --deep: #1a4f8c;
    --purple: #8a5cab;
    --glow-yellow: #f2d12d;
  }
  * { box-sizing: border-box; margin: 0; padding: 0; }
  html, body { width: 737px; height: 1200px; overflow: hidden; }
  body { background: var(--page); font-family: "Open Sans", Arial, sans-serif; color: var(--ink); position: relative; }
  .page { position: absolute; left: 10px; top: 8px; width: 717px; height: 1184px; }
  .abs { position: absolute; }

  /* header */
  .site-header { left: 0; top: 0; width: 717px; height: 95px; background: var(--white); border-top: 3px solid var(--navy); border-image: linear-gradient(90deg, var(--navy), var(--cyan)) 1; }
  .brand { left: 19px; top: 20px; display: flex; align-items: center; gap: 8px; }
  .brand-dot { width: 14px; height: 14px; border-radius: 50%; background: var(--brand); }
  .brand-name { font-size: 17px; line-height: 19px; font-weight: 400; color: var(--brand); letter-spacing: 0.5px; }
  .social { display: flex; gap: 5px; }
  .social span { width: 11px; height: 11px; border-radius: 50%; background: var(--brand); display: block; }
  .header-social { left: 464px; top: 28px; }
  .btn-signup { left: 508px; top: 19px; width: 93px; height: 19px; border: 2px solid var(--navy); border-radius: 10px; font-size: 9px; line-height: 15px; text-align: center; color: var(--ink); }
  .btn-login { left: 607px; top: 19px; width: 92px; height: 19px; border-radius: 10px; background: linear-gradient(180deg, var(--cyan), var(--navy)); font-size: 9px; line-height: 19px; text-align: center; color: var(--white); font-weight: 600; }
  .main-nav { right: 19px; top: 64px; display: flex; gap: 19px; font-size: 9px; font-weight: 600; }
  .main-nav a { color: var(--ink); text-decoration: none; padding-bottom: 5px; }
  .main-nav a.active { color: var(--accent); border-bottom: 2px solid var(--accent); }

  /* hero */
  .hero { left: 0; top: 95px; width: 717px; height: 400px; background: linear-gradient(180deg, #6f8fa0 0%, #3c6884 35%, #16406a 75%, #0e3560 100%); }
  .hero-copy { left: 0; top: 217px; width: 717px; text-align: center; color: var(--white); font-size: 17.5px; font-weight: 300; line-height: 23px; }
  .pillar { top: 261px; width: 90px; text-align: center; }
  .pillar-badge { width: 80px; height: 80px; margin: 0 auto; border-radius: 50%; box-shadow: 0 0 0 2px rgba(255,255,255,0.35); display: flex; align-items: center; justify-content: center; }
  .pillar-label { margin-top: 15px; color: var(--white); font-size: 11.5px; font-weight: 700; }

  /* about */
  .about { left: 0; top: 495px; width: 717px; height: 212px; background: linear-gradient(180deg, #f7f7f7, #e9e9e9); }
  .video-thumb { left: 52px; top: 39px; width: 219px; height: 142px; background: linear-gradient(160deg, #8b8a7e, #5a5a54 50%, #b9a95a); border: 3px solid var(--white); box-shadow: 0 1px 3px rgba(0,0,0,0.25); display: flex; align-items: center; justify-content: center; }
  .play { width: 40px; height: 40px; border-radius: 50%; background: rgba(0,0,0,0.55); display: flex; align-items: center; justify-content: center; }
  .about-title { left: 299px; top: 46px; font-family: "Roboto Condensed", Arial, sans-serif; font-weight: 700; font-size: 12px; letter-spacing: 0.3px; }
  .about-text { left: 299px; top: 70px; width: 380px; font-size: 10px; line-height: 15.5px; color: var(--body); }
  .btn-more { left: 299px; top: 127px; width: 88px; height: 26px; background: var(--navy); border-radius: 3px; color: var(--white); font-family: "Roboto Condensed", Arial, sans-serif; font-weight: 700; font-size: 10px; line-height: 26px; text-align: center; }

  /* features */
  .features { left: 0; top: 707px; width: 717px; height: 254px; background: linear-gradient(180deg, var(--band), var(--band-dark)); color: var(--white); }
  .features-title { left: 0; top: 26px; width: 717px; text-align: center; font-family: "Roboto Condensed", Arial, sans-serif; font-weight: 700; font-size: 12px; }
  .features-intro { left: 0; top: 50px; width: 717px; text-align: center; font-size: 10px; }
  .feature { top: 91px; width: 110px; text-align: center; }
  .feature-ring { width: 84px; height: 84px; margin: 0 auto; border-radius: 50%; border: 2px solid #f3c7f0; box-shadow: 0 0 6px 2px #d23fc9, inset 0 0 6px 1px #6b4bd8; display: flex; align-items: center; justify-content: center; }
  .feature-label { margin-top: 18px; font-family: "Roboto Condensed", Arial, sans-serif; font-weight: 700; font-size: 11px; line-height: 14.5px; }

  /* footer */
  .site-footer { left: 0; top: 961px; width: 717px; height: 191px; background: var(--white); }
  .footer-heading { font-size: 8px; font-weight: 700; color: var(--accent); }
  .footer-nav { left: 56px; top: 33px; }
  .footer-nav ul { list-style: none; margin-top: 8px; }
  .footer-nav li { font-size: 7px; font-weight: 600; color: var(--body); line-height: 13px; }
  .quick-contact { left: 209px; top: 33px; width: 134px; }
  .field { width: 134px; height: 15px; background: var(--field); font-size: 7.5px; color: var(--body); padding: 3px 7px; margin-top: 5px; }
  .field.message { height: 39px; }
  .btn-send { width: 64px; height: 23px; margin-top: 5px; background: var(--ink); color: var(--white); font-size: 9px; font-weight: 600; text-align: center; line-height: 23px; }
  .contact-info { left: 393px; top: 33px; }
  .contact-row { display: flex; gap: 8px; font-size: 7px; font-weight: 600; color: var(--body); line-height: 11.5px; margin-top: 8px; }
  .contact-row svg { flex: none; margin-top: 1px; }
  .footer-social { margin-top: 12px; }
  .footer-brand { left: 556px; top: 53px; }
  .copyright-bar { left: 0; top: 1152px; width: 717px; height: 32px; background: linear-gradient(180deg, #f6f6f6, #e4e4e4); font-size: 6.5px; font-weight: 600; color: var(--ink); text-align: center; line-height: 32px; }
</style>
</head>
<body>
<div class="page">

  <header class="site-header abs">
    <div class="brand abs">
      <span class="brand-dot"></span>
      <span class="brand-name">THE<br>HARBOR<br>LOFT</span>
    </div>
    <div class="social header-social abs" aria-label="Social links"><span></span><span></span></div>
    <div class="btn-signup abs">SIGN UP</div>
    <div class="btn-login abs">LOGIN</div>
    <nav class="main-nav abs">
      <a class="active">HOME</a>
      <a>WHAT IS THE HARBOR LOFT</a>
      <a>FEATURES</a>
      <a>CONTACT</a>
    </nav>
  </header>

  <section class="hero abs" role="img" aria-label="Photo of smiling business colleagues in a meeting">
    <p class="hero-copy abs">A unique destination for everything that practitioners need to execute best<br>practice change management, transformation and project methodologies.</p>

    <div class="pillar abs" style="left:89px">
      <div class="pillar-badge" style="background:var(--red)">
        <svg width="40" height="40" viewBox="0 0 40 40" stroke="#fff" stroke-width="2.5" fill="#fff"><line x1="20" y1="20" x2="7" y2="8"/><line x1="20" y1="20" x2="33" y2="8"/><line x1="20" y1="20" x2="6" y2="30"/><line x1="20" y1="20" x2="33" y2="31"/><line x1="20" y1="20" x2="20" y2="35"/><circle cx="20" cy="20" r="6"/><circle cx="7" cy="8" r="3"/><circle cx="33" cy="8" r="3"/><circle cx="6" cy="30" r="3"/><circle cx="33" cy="31" r="3"/><circle cx="20" cy="35" r="3"/></svg>
      </div>
      <div class="pillar-label">DYNAMIC</div>
    </div>
    <div class="pillar abs" style="left:206px">
      <div class="pillar-badge" style="background:var(--yellow)">
        <svg width="40" height="36" viewBox="0 0 40 36" fill="#fff"><path d="M2 3h22v15H11l-6 5v-5H2z"/><path d="M16 13h22v14h-3v5l-6-5H16z" fill="#fff" stroke="var(--yellow)" stroke-width="2"/></svg>
      </div>
      <div class="pillar-label">PERSONAL</div>
    </div>
    <div class="pillar abs" style="left:323px">
      <div class="pillar-badge" style="background:var(--blue)">
        <svg width="42" height="32" viewBox="0 0 42 32" fill="#fff"><path d="M2 3q9-3 18 1v26q-9-4-18-1z"/><path d="M22 4q9-4 18-1v26q-9-3-18 1z"/><g stroke="var(--blue)" stroke-width="2"><line x1="6" y1="10" x2="16" y2="10"/><line x1="6" y1="16" x2="16" y2="16"/><line x1="6" y1="22" x2="16" y2="22"/><line x1="26" y1="10" x2="36" y2="10"/><line x1="26" y1="16" x2="36" y2="16"/><line x1="26" y1="22" x2="36" y2="22"/></g></svg>
      </div>
      <div class="pillar-label">LEARNING</div>
    </div>
    <div class="pillar abs" style="left:440px">
      <div class="pillar-badge" style="background:var(--deep)">
        <svg width="40" height="40" viewBox="0 0 40 40" fill="none" stroke="#fff" stroke-width="4"><rect x="4" y="18" width="18" height="10" rx="5" transform="rotate(-45 13 23)"/><rect x="18" y="12" width="18" height="10" rx="5" transform="rotate(-45 27 17)"/></svg>
      </div>
      <div class="pillar-label">CONNECTED</div>
    </div>
    <div class="pillar abs" style="left:557px">
      <div class="pillar-badge" style="background:var(--purple)">
        <svg width="36" height="36" viewBox="0 0 36 36" fill="#fff" stroke="#fff" stroke-width="3"><line x1="9" y1="18" x2="27" y2="8"/><line x1="9" y1="18" x2="27" y2="28"/><circle cx="9" cy="18" r="5"/><circle cx="27" cy="8" r="5"/><circle cx="27" cy="28" r="5"/></svg>
      </div>
      <div class="pillar-label">VIBRANT</div>
    </div>
  </section>

  <section class="about abs">
    <div class="video-thumb abs" role="img" aria-label="Video still of a group seated in a circle workshop">
      <div class="play"><svg width="16" height="18" viewBox="0 0 16 18"><path d="M2 1l13 8-13 8z" fill="#fff"/></svg></div>
    </div>
    <h2 class="about-title abs">WHAT IS THE HARBOR LOFT</h2>
    <p class="about-text abs">The Harbor Loft's offering will be positioned as a place of learning, connecting, collaborating and sharing. It's a resource for change professional to further the conversation around change.</p>
    <div class="btn-more abs">READ MORE</div>
  </section>

  <section class="features abs">
    <h2 class="features-title abs">FEATURES</h2>
    <p class="features-intro abs">The Harbor Loft is a ‘community’ whereby an individual can go to learn, connect, collaborate and share, where you will be able to</p>

    <div class="feature abs" style="left:38px">
      <div class="feature-ring"><svg width="48" height="48" viewBox="0 0 48 48" fill="var(--glow-yellow)"><circle cx="24" cy="15" r="10"/><path d="M4 44q2-17 20-17t20 17z"/></svg></div>
      <div class="feature-label">UPLOAD YOUR<br>PROFILE</div>
    </div>
    <div class="feature abs" style="left:148px">
      <div class="feature-ring"><svg width="40" height="48" viewBox="0 0 40 48" fill="none" stroke="var(--glow-yellow)" stroke-width="3"><rect x="3" y="6" width="34" height="39" rx="2"/><rect x="13" y="2" width="14" height="7" fill="var(--glow-yellow)"/><path d="M9 18l3 3 5-5M9 28l3 3 5-5M9 38l3 3 5-5"/><path d="M21 19h11M21 29h11M21 39h11"/></svg></div>
      <div class="feature-label">GAIN ACCESS TO<br>TRAINING<br>INFORMATION</div>
    </div>
    <div class="feature abs" style="left:259px">
      <div class="feature-ring"><svg width="50" height="46" viewBox="0 0 50 46" fill="var(--glow-yellow)"><rect x="22" y="3" width="24" height="16" fill="none" stroke="var(--glow-yellow)" stroke-width="2"/><rect x="27" y="11" width="3" height="6"/><rect x="32" y="8" width="3" height="9"/><rect x="37" y="6" width="3" height="11"/><circle cx="12" cy="8" r="4"/><rect x="8" y="13" width="8" height="10"/><circle cx="9" cy="30" r="4"/><circle cx="25" cy="30" r="4"/><circle cx="41" cy="30" r="4"/><path d="M3 44q0-9 6-9t6 9zM19 44q0-9 6-9t6 9zM35 44q0-9 6-9t6 9z"/></svg></div>
      <div class="feature-label">UPCOMING EVENTS,<br>SPEAKERS &amp;<br>WEBINARS</div>
    </div>
    <div class="feature abs" style="left:369px">
      <div class="feature-ring"><svg width="48" height="48" viewBox="0 0 48 48" fill="none" stroke="var(--glow-yellow)" stroke-width="4"><circle cx="24" cy="24" r="8"/><path d="M20 4h8l1 6 5 2 5-4 5 5-4 5 2 5 6 1v8l-6 1-2 5 4 5-5 5-5-4-5 2-1 6h-8l-1-6-5-2-5 4-5-5 4-5-2-5-6-1v-8l6-1 2-5-4-5 5-5 5 4 5-2z" stroke-linejoin="round"/></svg></div>
      <div class="feature-label">ACCESS TO<br>TOOLS &amp;<br>TEMPLATES</div>
    </div>
    <div class="feature abs" style="left:479px">
      <div class="feature-ring"><svg width="48" height="46" viewBox="0 0 48 46" fill="none" stroke="var(--glow-yellow)" stroke-width="3.5"><path d="M4 4h40v28H22l-9 9v-9H4z" stroke-linejoin="round"/><path d="M24 9l3 7h7l-6 4 2 7-6-4-6 4 2-7-6-4h7z" fill="var(--glow-yellow)" stroke="none"/></svg></div>
      <div class="feature-label">GAIN FURTHER<br>ACCREDITATION</div>
    </div>
    <div class="feature abs" style="left:590px">
      <div class="feature-ring"><svg width="46" height="46" viewBox="0 0 46 46" fill="var(--glow-yellow)"><rect x="2" y="34" width="12" height="10"/><rect x="15" y="26" width="12" height="18"/><rect x="28" y="16" width="14" height="28"/><circle cx="30" cy="5" r="4"/><path d="M24 22l4-12 5 2 3 6-3 1-2-3-3 8z"/></svg></div>
      <div class="feature-label">GET ACCESS<br>TO COACHING</div>
    </div>
  </section>

  <footer class="site-footer abs">
    <div class="footer-nav abs">
      <div class="footer-heading">NAVIGATION</div>
      <ul><li>HOME</li><li>WHAT IS THE HARBOR LOFT</li><li>FEATURES</li><li>CONTACT</li></ul>
    </div>
    <div class="quick-contact abs">
      <div class="footer-heading">QUICK CONTACT</div>
      <div class="field">Name</div>
      <div class="field">Email</div>
      <div class="field">Phone</div>
      <div class="field message">Message</div>
      <div class="btn-send">SEND</div>
    </div>
    <div class="contact-info abs">
      <div class="footer-heading">CONTACT</div>
      <div class="contact-row">
        <svg width="9" height="12" viewBox="0 0 9 12"><path d="M4.5 0a4.5 4.5 0 0 1 4.5 4.5c0 3-4.5 7.5-4.5 7.5S0 7.5 0 4.5A4.5 4.5 0 0 1 4.5 0z" fill="#444"/><circle cx="4.5" cy="4.5" r="1.7" fill="#fff"/></svg>
        <span>THE HARBOR LOFT<br>48 QUAYSIDE LANE<br>PORT ALDER</span>
      </div>
      <div class="contact-row" style="margin-top:12px">
        <svg width="11" height="9" viewBox="0 0 11 9"><path d="M1 3q4.5-4 9 0l-2 1-1-1H4L3 4z" fill="#444"/><rect x="2" y="4" width="7" height="5" rx="1" fill="#444"/></svg>
        <span>(555)014-2270</span>
      </div>
      <div class="contact-row" style="margin-top:12px">
        <svg width="11" height="8" viewBox="0 0 11 8"><rect x="0.5" y="0.5" width="10" height="7" fill="none" stroke="#444"/><path d="M0.5 0.5l5 4 5-4" fill="none" stroke="#444"/></svg>
        <span>info@harborloft.example</span>
      </div>
      <div class="social footer-social" aria-label="Social links"><span></span><span></span></div>
    </div>
    <div class="brand footer-brand abs">
      <span class="brand-dot"></span>
      <span class="brand-name">THE<br>HARBOR<br>LOFT</span>
    </div>
  </footer>

  <div class="copyright-bar abs">COPYRIGHT © 2016 THE HARBOR LOFT. ALL RIGHTS RESERVED</div>
</div>
</body>
</html>
```